Larkspur Ridge Management - Business Cards

I need business cards. My current logo was designed by a designer at this site and I very much like and am happy with the results. I would like a business card that is trendy, unique, current yet professional. I deal with high net worth clients daily

Target Market(s)

Out of state investors looking to get into the rental market in Ohio

Industry/Entity Type

Property Management, Consulting

Contact Information for Business Card

Name, Title (Chief Financial Officer) office phone number (555) 817-3094 website address larkridgemgmt.example

Font styles to use
Sans Serif

Colors
0054AA
0677BA
7BADD7
CADEEF
E8F1F8
0094D4
00A9DD
6FCCEA
C7EBF8
E9F6FB
00AB8E
00BBA5
67D7C9
C6EFE9
E9F9F6

```html
<!DOCTYPE html>
<html lang="en">
<head>
<meta charset="utf-8">
<title>Larkspur Ridge Management – Business Cards</title>
<link rel="stylesheet" href="https://fonts.googleapis.com/css2?family=Inter:wght@400;600;800&display=swap">
<style>
  :root {
    --backdrop: #e6e3de;
    --card: #f8f6f1;
    --navy: #1f2f5c;
    --red: #c8202f;
    --ink: #26304a;
  }
  * { box-sizing: border-box; margin: 0; padding: 0; }
  html, body {
    width: 1200px;
    height: 1200px;
    overflow: hidden;
    background: var(--backdrop);
    font-family: "Inter", sans-serif;
  }
  .canvas { position: relative; width: 1200px; height: 1200px; }

  .card {
    position: absolute;
    top: 220px;
    width: 454px;
    height: 739px;
    background: var(--card);
    box-shadow: 0 2px 6px rgba(0,0,0,0.08);
  }
  .card-front { left: 121px; border-radius: 18px; }
  .card-back { left: 641px; border-radius: 3px; }

  /* Front */
  .wordmark {
    position: absolute;
    left: 0; right: 0;
    top: 180px;
    text-align: center;
    color: var(--navy);
    font-weight: 800;
    font-size: 42px;
    line-height: 1.12;
    letter-spacing: 0.5px;
    text-transform: uppercase;
  }
  .wordmark-square {
    display: block;
    width: 130px; height: 130px;
    margin: 0 auto 34px;
    background: var(--navy);
  }
  .front-rule {
    position: absolute;
    left: 75px; width: 302px;
    top: 555px;
    height: 2px;
    background: var(--red);
  }

  /* Back */
  .back-frame {
    position: absolute;
    inset: 18px 20px 18px 19px;
    border: 2px solid var(--navy);
  }
  .contact {
    position: absolute;
    right: 61px;
    top: 245px;
    text-align: right;
    color: var(--ink);
  }
  .contact-name {
    font-weight: 600;
    font-size: 35px;
    color: var(--navy);
    line-height: 1.1;
  }
  .contact-title {
    font-weight: 400;
    font-size: 25px;
    margin-top: 14px;
  }
  .contact-rule {
    width: 311px;
    height: 2px;
    background: var(--red);
    margin: 38px 0 38px auto;
  }
  .contact-phone, .contact-web {
    font-size: 27px;
    font-weight: 400;
    line-height: 1.65;
  }
</style>
</head>
<body>
<main class="canvas">
  <section class="card card-front">
    <div class="wordmark">
      <span class="wordmark-square"></span>
      Larkspur Ridge<br>Management
    </div>
    <div class="front-rule"></div>
  </section>

  <section class="card card-back">
    <div class="back-frame"></div>
    <div class="contact">
      <p class="contact-name">Daniel Moreau</p>
      <p class="contact-title">Chief Financial Officer</p>
      <div class="contact-rule"></div>
      <p class="contact-phone">(555) 817-3094</p>
      <p class="contact-web">larkridgemgmt.example</p>
    </div>
  </section>
</main>
</body>
</html>
```